A5 Merchandise Sale Flyer for CPR Face Mask Keyrings

We are a Registered Training Orgniastion (RTO 48317) who specialises in delivering health programs inclusive of First Aid and we would like to have a A5 flyer created to advertise/sell our CPR Face Sheild Keyrings to our students and the greater public.
We would like to flyer to be engaging, modern and fun - ultimately, we want to get a sale!

*The cost of a CPR Face Sheild Keyring is $7.00.

*Website, phone number and address to be included on flyer - please emphaise website

www.brightmendcourses.edu.au
03 9561 2748
Level 2, 14 Tamsin Street, Blackburn VIC 3130

*We want our logo and RTO number (as bove) to be included on the flyer also emphaised

*Keep within our company colours
*Use some or one of the attahed photographs
*Use image of CPR face sheild keyring

*Please include payment can be made at Brightmend Courses Reception.

Thanks!

Target Market(s)

Students & Wider Public

Industry/Entity Type

Health

Font styles to use
Serif
Sans Serif
Decorative

Colors
f37122
faa54b
ffc214

Requirements
Must have
• Company Colours, logo and company details emphaises on website, price of product, iamge of product and a tagline.

```html
<!DOCTYPE html>
<html lang="en">
<head>
<meta charset="utf-8">
<title>Brightmend Courses – CPR Face Shield Keyring</title>
<link rel="stylesheet" href="https://fonts.googleapis.com/css2?family=Source+Sans+3:wght@400;600;700&display=swap">
<style>
  :root {
    --orange: #f37122;
    --orange-light: #faa54b;
    --yellow: #ffc214;
    --ink: #2b2b2b;
    --green: #1f9e3a;
    --white: #ffffff;
  }
  * { box-sizing: border-box; margin: 0; padding: 0; }
  html, body { width: 849px; height: 1200px; overflow: hidden; background: #fff; }
  body { font-family: "Source Sans 3", Arial, sans-serif; color: var(--ink); }
  .flyer { position: relative; width: 849px; height: 1200px; overflow: hidden; background: var(--white); }

  .brand { position: absolute; left: 66px; top: 10px; width: 110px; }
  .brand-dot { display: block; width: 84px; height: 84px; margin: 0 0 0 10px; border-radius: 50%; background: var(--yellow); }
  .brand-name { margin-top: 18px; font-size: 23px; font-weight: 600; line-height: 1.02; color: var(--orange); }
  .rule-stub { position: absolute; left: 0; top: 106px; width: 62px; height: 5px; background: var(--yellow); }

  .website { position: absolute; left: 444px; top: 36px; font-size: 25px; color: var(--ink); }
  .website .domain { color: var(--orange); }
  .rule { position: absolute; height: 6px; background: var(--yellow); }
  .rule-top { left: 322px; right: 0; top: 103px; }
  .rule-mid { left: 0; right: 0; top: 568px; }

  .price-panel {
    position: absolute; left: 0; top: 176px; width: 368px; height: 379px;
    background: linear-gradient(160deg, var(--orange-light), var(--orange) 55%);
    box-shadow: 4px 5px 8px rgba(0,0,0,0.35);
    color: var(--white); text-align: center; padding-top: 38px;
  }
  .price-title { font-size: 44px; font-weight: 700; line-height: 1.4; text-shadow: 1px 2px 3px rgba(0,0,0,0.3); }
  .price-amount { font-size: 104px; font-weight: 700; line-height: 1; margin-top: 14px; text-shadow: 2px 3px 4px rgba(0,0,0,0.3); }
  .price-note { font-size: 13px; line-height: 1.3; margin-top: 20px; }

  .product-photo {
    position: absolute; left: 392px; top: 128px; width: 457px; height: 427px;
    background:
      radial-gradient(ellipse 90px 62px at 250px 72px, #f47b20 0%, #f47b20 70%, rgba(244,123,32,0) 100%),
      radial-gradient(ellipse 98px 66px at 250px 210px, #f37122 0%, #f37122 70%, rgba(243,113,34,0) 100%),
      radial-gradient(ellipse 98px 66px at 322px 342px, #f47b20 0%, #f47b20 70%, rgba(244,123,32,0) 100%),
      linear-gradient(180deg, #ffffff, #f7f7f7);
  }

  .feature { position: absolute; left: 15px; width: 520px; height: 147px; }
  .feature-photo { position: absolute; left: 0; top: 0; width: 221px; height: 147px; }
  .feature-text { position: absolute; left: 231px; top: 34px; width: 270px; }
  .feature h2 { font-size: 21px; font-weight: 700; color: var(--orange); margin-bottom: 12px; line-height: 1.1; }
  .feature p { font-size: 9.5px; line-height: 1.4; color: var(--ink); }
  .feature-1 { top: 604px; }
  .feature-2 { top: 757px; } .feature-2 .feature-text { top: 37px; }
  .feature-3 { top: 919px; } .feature-3 .feature-text { top: 35px; }
  .photo-class { background:
      radial-gradient(ellipse 60px 30px at 120px 110px, #d3302a 0%, rgba(211,48,42,0) 100%),
      linear-gradient(135deg, #6f6a66 0%, #bdb3aa 45%, #e2ddd8 100%); }
  .photo-student { background:
      radial-gradient(ellipse 50px 60px at 60px 85px, #7a4e36 0%, rgba(122,78,54,0) 100%),
      linear-gradient(135deg, #e9e7e4 0%, #d6d2ce 60%, #a7a09a 100%); }
  .photo-practice { background:
      radial-gradient(ellipse 70px 45px at 110px 85px, #d9b39a 0%, rgba(217,179,154,0) 100%),
      linear-gradient(135deg, #f1e4da 0%, #d8b8a3 55%, #8c7b72 100%); }

  .mission {
    position: absolute; left: 547px; top: 647px; width: 300px;
    font-size: 29px; line-height: 37.5px; color: var(--orange);
  }
  .first-aid { position: absolute; left: 642px; top: 974px; width: 60px; height: 70px; }

  .contact { position: absolute; left: 0; top: 1108px; width: 849px; height: 92px; color: var(--white); text-align: center; }
  .contact svg { position: absolute; left: 0; top: 0; }
  .contact-text { position: relative; padding-top: 20px; font-size: 15px; line-height: 1.3; }
  .contact-text h3 { font-size: 17px; font-weight: 700; }
</style>
</head>
<body>
<main class="flyer">
  <header>
    <div class="brand">
      <span class="brand-dot"></span>
      <p class="brand-name">Brightmend<br>Courses</p>
    </div>
    <div class="rule-stub"></div>
    <p class="website">www.<span class="domain">brightmendcourses</span>.edu.au</p>
    <div class="rule rule-top"></div>
  </header>

  <section class="price-panel">
    <h1 class="price-title">CPR Face<br>Sheild Keyring</h1>
    <p class="price-amount">$7.00</p>
    <p class="price-note">( Payment can be made at<br>Brightmend Courses<br>Reception )</p>
  </section>

  <div class="product-photo" role="img" aria-label="Three orange CPR face shield keyring pouches with black trim and metal rings on white"></div>

  <div class="rule rule-mid"></div>

  <section class="feature feature-1">
    <div class="feature-photo photo-class" role="img" aria-label="Students practising CPR on a training manikin in class"></div>
    <div class="feature-text">
      <h2>New Courses for 2015</h2>
      <p>We offer a range of Certificate Courses in Pathology,<br>Aged Care, Health Services Assitance,<br>Home &amp; Community Care.</p>
    </div>
  </section>

  <section class="feature feature-2">
    <div class="feature-photo photo-student" role="img" aria-label="Smiling student in a classroom"></div>
    <div class="feature-text">
      <h2>The Course for your Career</h2>
      <p>Apply now for certificate courses commencing soon at<br>one of our four Melbourne locations in areas such as<br>Aged Care, Health Services and Pathology.</p>
    </div>
  </section>

  <section class="feature feature-3">
    <div class="feature-photo photo-practice" role="img" aria-label="Hands performing chest compressions on a CPR manikin"></div>
    <div class="feature-text">
      <h2>Careers in Phlebotomy</h2>
      <p>This course is designed to be an entry level for those<br>wishing to pursue a career in the Pathology Specimen<br>Collection Industry.</p>
    </div>
  </section>

  <p class="mission">We are a Registered<br>Training Organization<br>(RTO 48317)<br>who specialises in<br>delivering health<br>programs inclusive<br>of First Aid</p>

  <svg class="first-aid" viewBox="0 0 60 70" aria-label="First aid sign">
    <rect x="0.5" y="0.5" width="59" height="69" fill="#fff" stroke="#bbb" stroke-width="1"/>
    <rect x="4" y="4" width="52" height="46" fill="var(--green)"/>
    <rect x="24" y="11" width="12" height="32" fill="#fff"/>
    <rect x="14" y="21" width="32" height="12" fill="#fff"/>
    <rect x="4" y="53" width="52" height="13" fill="var(--green)"/>
    <text x="30" y="62.5" text-anchor="middle" font-family="Source Sans 3, Arial, sans-serif" font-size="8" font-weight="700" fill="#fff">FIRST AID</text>
  </svg>

  <footer class="contact">
    <svg width="849" height="92" viewBox="0 0 849 92" aria-hidden="true">
      <defs>
        <linearGradient id="footerFill" x1="0" y1="0" x2="0" y2="1">
          <stop offset="0" stop-color="#faa54b"/>
          <stop offset="1" stop-color="#f37122"/>
        </linearGradient>
      </defs>
      <path d="M0 40 Q424 -30 849 40 L849 92 L0 92 Z" fill="url(#footerFill)"/>
    </svg>
    <div class="contact-text">
      <h3>Contact Us</h3>
      <p>03 9561 2748</p>
      <p>Level 2, 14 Tamsin Street, Blackburn VIC 3130</p>
    </div>
  </footer>
</main>
</body>
</html>
```